Business Card Design

We are a manufacturing and distribution company with most of our customer base being supermarkets. We have established brand guidelines that are attached.

```html
<!DOCTYPE html>
<html lang="en">
<head>
<meta charset="utf-8">
<title>Korvale Business Card</title>
<link href="https://fonts.googleapis.com/css2?family=Montserrat:wght@700&family=Arimo:wght@400;700&display=swap" rel="stylesheet">
<style>
  :root {
    --backdrop: #2b2b2b;
    --card: #0d0d0d;
    --ink: #f2f2f2;
    --ink-soft: #bdbdbd;
    --red: #e0202c;
    --blue: #1f7ac4;
    --rule: #4a4a4a;
  }
  * { box-sizing: border-box; margin: 0; padding: 0; }
  html, body { width: 1200px; height: 900px; overflow: hidden; }
  body {
    background: var(--backdrop);
    font-family: "Arimo", Arial, sans-serif;
    display: flex;
    align-items: center;
    justify-content: center;
    gap: 40px;
  }
  .card {
    width: 540px;
    height: 309px;
    background: var(--card);
    border-radius: 20px;
    position: relative;
    overflow: hidden;
  }
  /* Front */
  .card-front { display: flex; align-items: center; }
  .brand-block {
    width: 52%;
    display: flex;
    align-items: center;
    justify-content: center;
    gap: 12px;
  }
  .brand-mark {
    width: 26px; height: 26px;
    background: var(--red);
  }
  .brand-name {
    font-family: "Montserrat", Arial, sans-serif;
    font-weight: 700;
    color: var(--ink);
    font-size: 32px;
    letter-spacing: 2px;
  }
  .divider {
    width: 1px;
    height: 170px;
    background: var(--rule);
  }
  .contact-block {
    padding-left: 26px;
    color: var(--ink);
    font-size: 13px;
    line-height: 1.3;
  }
  .person-name {
    font-family: "Montserrat", Arial, sans-serif;
    font-weight: 700;
    font-size: 17px;
    letter-spacing: 0.5px;
  }
  .person-name .first { color: var(--red); }
  .person-name .last { color: var(--blue); }
  .person-role { font-size: 13px; margin-bottom: 12px; }
  .contact-list { list-style: none; margin-bottom: 12px; }
  .contact-list li { display: flex; align-items: center; gap: 7px; margin-bottom: 2px; }
  .contact-list svg { width: 12px; height: 12px; flex: none; }
  .web-accent { color: var(--blue); }
  .address { font-size: 13px; }
  /* Back */
  .card-back {
    display: flex;
    align-items: center;
    justify-content: center;
    gap: 14px;
  }
  .card-back .brand-mark { background: var(--ink); width: 24px; height: 24px; }
  .card-back .brand-name { color: var(--ink-soft); font-size: 30px; }
</style>
</head>
<body>
  <section class="card card-front">
    <div class="brand-block">
      <span class="brand-mark"></span>
      <span class="brand-name">KORVALE</span>
    </div>
    <div class="divider"></div>
    <div class="contact-block">
      <p class="person-name"><span class="first">DANIEL</span> <span class="last">HARROW</span></p>
      <p class="person-role">Managing Director</p>
      <ul class="contact-list">
        <li>
          <svg viewBox="0 0 24 24" aria-hidden="true"><path fill="var(--red)" d="M6.6 10.8a15.1 15.1 0 0 0 6.6 6.6l2.2-2.2c.3-.3.7-.4 1-.2 1.1.4 2.3.6 3.6.6.6 0 1 .4 1 1V20c0 .6-.4 1-1 1A17 17 0 0 1 3 4c0-.6.4-1 1-1h3.5c.6 0 1 .4 1 1 0 1.3.2 2.5.6 3.6.1.3 0 .7-.2 1z"/></svg>
          055-210 384 617
        </li>
        <li>
          <svg viewBox="0 0 24 24" aria-hidden="true"><path fill="var(--red)" d="M2 5h20v14H2z"/><path fill="none" stroke="var(--card)" stroke-width="1.6" d="M2 5l10 8 10-8"/></svg>
          hello@korvale.com
        </li>
        <li>
          <svg viewBox="0 0 24 24" aria-hidden="true"><g fill="none" stroke="var(--red)" stroke-width="2"><circle cx="12" cy="12" r="10"/><ellipse cx="12" cy="12" rx="4" ry="10"/><path d="M2 12h20M4 7h16M4 17h16"/></g></svg>
          www.<span class="web-accent">korvale</span>.com
        </li>
      </ul>
      <p class="address">88, Mill Road Trading Estate<br>30718, Northland</p>
    </div>
  </section>

  <section class="card card-back">
    <span class="brand-mark"></span>
    <span class="brand-name">KORVALE</span>
  </section>
</body>
</html>
```